VoIP Unified Communications Service Flyer

I need a trifold brochure made for my VoIP services describing the advantages of switching over to VoIP Unified Communications, I want our current logo, and contact info, as well as the color scheme that we use with the logo, which is gray, and orange, also a picture of the Brontel KX-M41D phone should be used as an example of the phones we provide. The trifold brochure should be printable on 8.5 by 11inch paper, I uploaded some of the images that if modified so I am not plagiarizing, could help for the 3 inner folds.

Target Market(s)

Businesses

Industry/Entity Type

Telecommunications

Font styles to use
Serif
Sans Serif

Requirements
Must have
• Top Reasons to move to VoIP Unified Communications Service, a picture of a Brontel KX-M41D Phone, contact info on the back, company name and logo in the top, one of the reasons should be, we are a local company, and we offer immediate US based support.
Nice to have
• Contact info:

O: (575) 648-3105
C: (575) 702-8846
E: info@pelomarcsystems.com
W: https://pelomarcsystems.com
FB: https://facebook.com/pelomarcsystems

```html
<!DOCTYPE html>
<html lang="en">
<head>
<meta charset="utf-8">
<title>Pelomarc Systems – VoIP Trifold Brochure</title>
<link rel="stylesheet" href="https://fonts.googleapis.com/css2?family=Oswald:wght@300;500;600&family=Montserrat:wght@400;500;600&display=swap">
<style>
:root{
  --bg:#74d1b4;
  --orange:#f26f33;
  --dark:#1f1d1e;
  --ink:#2c2c2c;
  --grey-panel:#e6e6e6;
  --white:#ffffff;
  --logo-grey:#8a8d91;
}
*{box-sizing:border-box;margin:0;padding:0}
html,body{width:1200px;height:2925px;overflow:hidden}
body{background:var(--bg);font-family:"Montserrat",sans-serif;color:var(--ink);position:relative}
.spread{position:absolute;left:122px;width:956px;background:var(--white)}
.spread--outer{top:1150px;height:743px}
.spread--inner{top:1993px;height:745px}
.abs{position:absolute}

.band{background:var(--orange);color:var(--white);font-family:"Oswald",sans-serif;font-weight:500;display:flex;align-items:center}
.band--about{left:0;top:0;width:318px;height:63px;padding-left:32px;font-size:22px;letter-spacing:7px}
.copy{font-size:9.4px;line-height:1.28;color:var(--ink)}
.heading{font-family:"Oswald",sans-serif;font-weight:600;color:var(--orange);font-size:21px;line-height:1.28;text-transform:uppercase;letter-spacing:-.2px}
.photo{background:linear-gradient(135deg,#dfe3e6,#bfc5ca 55%,#8f969c)}
.photo--city{background:linear-gradient(120deg,#6c87a6 0%,#2b4b78 40%,#1a2f58 70%,#3a5f97 100%)}
.grey-panel{background:var(--grey-panel)}
.dark-panel{background:var(--dark);color:var(--white)}
.orange-panel{background:var(--orange);color:var(--white)}

.logo{display:flex;align-items:center;gap:8px;font-family:"Montserrat",sans-serif;font-weight:600;color:var(--orange);letter-spacing:2px;text-transform:uppercase;white-space:nowrap}
.logo__mark{width:16px;height:16px;border-radius:50%;background:var(--logo-grey);flex:none}

.contact{text-align:center}
.contact__title{font-weight:600;font-size:21px;margin-top:14px}
.contact__icons{display:flex;justify-content:center;gap:27px;margin:14px 0 14px}
.contact__icon{width:27px;height:27px;border-radius:50%;background:var(--orange);display:flex;align-items:center;justify-content:center}
.contact__line{font-size:12.5px;line-height:21.5px}
.contact__social{display:flex;justify-content:center;align-items:center;gap:10px;font-size:12.5px;margin-top:9px}
.contact__social-mark{width:17px;height:17px;background:#3b5ea8}

.hero-title{font-family:"Oswald",sans-serif;text-align:center;text-transform:uppercase}
.hero-title__light{font-weight:300;font-size:44px;line-height:1;display:block;transform:scaleX(.92)}
.hero-title__bold{font-weight:600;font-size:76px;line-height:.8;display:block;letter-spacing:-1px}
.hero-rule{width:150px;height:2px;background:var(--white);margin:0 auto}
.hero-tag{font-size:15px;font-weight:500;line-height:1.25;text-align:center}

.band--reasons{left:0;top:0;width:956px;height:64px;justify-content:center;font-size:21px;letter-spacing:6.3px}
.reason{position:absolute;width:260px;text-align:center}
.reason__icon{width:50px;height:50px;margin:0 auto 7px;border-radius:50%;background:radial-gradient(circle at 50% 55%,#f7a23a 0 30%,#3a3a3a 31% 38%,#fff 39%)}
.reason__title{font-weight:600;color:var(--orange);font-size:14.5px;margin-bottom:6px}
.reason__text{font-size:9.2px;line-height:1.27;color:var(--ink)}
.desk-phone{background:radial-gradient(ellipse at 55% 55%,#3a3b3d 0 45%,#cfcfc9 46% 52%,#ffffff 70%)}
</style>
</head>
<body>

<!-- Outer spread -->
<section class="spread spread--outer">
  <div class="band band--about abs">ABOUT US</div>
  <p class="copy abs" style="left:32px;top:91px;width:252px">We’re inspired by our clients and work to advance their business by innovating everything digital. We’re endless innovators, constantly looking for new ways to connect the dots and connect people. We become part of your team, true partners with a sustained commitment to your business goals.</p>
  <h2 class="heading abs" style="left:32px;top:200px;font-size:22px">OUR VISION &amp; VALUES</h2>
  <p class="copy abs" style="left:32px;top:238px;width:252px">Customer satisfaction, openness, innovation, teamwork and growth are the core values behind our company. We continue to reflect who we are, how we work, and what we strive for.</p>
  <div class="photo abs" role="img" aria-label="Hand dialling an office desk phone" style="left:0;top:305px;width:318px;height:207px"></div>
  <div class="grey-panel abs" style="left:0;top:512px;width:318px;height:231px"></div>
  <h2 class="heading abs" style="left:32px;top:535px;width:270px">COLLABORATION AND UNIFIED COMMUNICATIONS</h2>
  <p class="copy abs" style="left:32px;top:611px;width:252px">Communication and collaboration. It’s how work gets done. We provide next generation phone services known as VoIP, as well as Unified Communications Services that will help you accomplish your business goals more efficiently, and help you gain an edge against your competition, and possibly help you save money, that could be used elsewhere in your business.</p>

  <div class="photo--city abs" role="img" aria-label="Business hand touching a VoIP hexagon interface over a city skyline" style="left:318px;top:0;width:638px;height:428px"></div>

  <div class="dark-panel abs" style="left:632px;top:372px;width:324px;height:56px;display:flex;align-items:center;justify-content:center">
    <div class="logo" style="font-size:14px"><span class="logo__mark"></span>Pelomarc Systems</div>
  </div>

  <div class="dark-panel abs contact" style="left:318px;top:428px;width:314px;height:315px;padding-top:36px">
    <div class="logo" style="justify-content:center;font-size:13px"><span class="logo__mark"></span>Pelomarc Systems</div>
    <div class="contact__title">Contact us</div>
    <div class="contact__icons">
      <span class="contact__icon"><svg width="14" height="14" viewBox="0 0 24 24"><path fill="#fff" d="M6.6 10.8a15 15 0 0 0 6.6 6.6l2.2-2.2a1 1 0 0 1 1-.25 11.4 11.4 0 0 0 3.6.57 1 1 0 0 1 1 1V20a1 1 0 0 1-1 1A17 17 0 0 1 3 4a1 1 0 0 1 1-1h3.5a1 1 0 0 1 1 1c0 1.25.2 2.45.57 3.57a1 1 0 0 1-.25 1z"/></svg></span>
      <span class="contact__icon"><svg width="14" height="14" viewBox="0 0 24 24"><path fill="#fff" d="M6.6 10.8a15 15 0 0 0 6.6 6.6l2.2-2.2a1 1 0 0 1 1-.25 11.4 11.4 0 0 0 3.6.57 1 1 0 0 1 1 1V20a1 1 0 0 1-1 1A17 17 0 0 1 3 4a1 1 0 0 1 1-1h3.5a1 1 0 0 1 1 1c0 1.25.2 2.45.57 3.57a1 1 0 0 1-.25 1z"/></svg></span>
      <span class="contact__icon"><svg width="14" height="14" viewBox="0 0 24 24"><rect x="3" y="6" width="18" height="12" fill="none" stroke="#fff" stroke-width="2"/><path d="M3 6l9 7 9-7" fill="none" stroke="#fff" stroke-width="2"/></svg></span>
      <span class="contact__icon"><svg width="14" height="14" viewBox="0 0 24 24"><circle cx="12" cy="12" r="9" fill="none" stroke="#fff" stroke-width="2"/><path d="M3 12h18M12 3c3 3 3 15 0 18M12 3c-3 3-3 15 0 18" fill="none" stroke="#fff" stroke-width="1.6"/></svg></span>
    </div>
    <div class="contact__line">(575) 648-3105</div>
    <div class="contact__line">(575) 702-8846</div>
    <div class="contact__line">info@pelomarcsystems.com</div>
    <div class="contact__line">www.pelomarcsystems.com</div>
    <div class="contact__social"><span class="contact__social-mark"></span>pelomarcsystems</div>
  </div>

  <div class="orange-panel abs" style="left:632px;top:428px;width:324px;height:315px;padding-top:30px">
    <h1 class="hero-title">
      <span class="hero-title__light">Professional</span>
      <span class="hero-title__bold">VoIP</span>
      <span class="hero-title__bold">Services</span>
    </h1>
    <div class="hero-rule" style="margin-top:22px"></div>
    <p class="hero-tag" style="margin-top:12px">We are a local company, and<br>we offer immediate US based<br>support.</p>
  </div>
</section>

<!-- Inner spread -->
<section class="spread spread--inner">
  <div class="band band--reasons abs">REASONS TO MOVE TO VOIP UNIFIED COMMUNICATIONS SERVICE</div>

  <div class="reason" style="left:29px;top:88px">
    <div class="reason__icon" role="img" aria-label="Piggy bank icon"></div>
    <div class="reason__title">Saves you money</div>
    <p class="reason__text">Customers of Corvanta’s small business VoIP phone service typically experience savings of up to 60% on their monthly phone bill.</p>
  </div>
  <div class="reason" style="left:29px;top:238px">
    <div class="reason__icon" role="img" aria-label="Secure network icon"></div>
    <div class="reason__title">Secure network</div>
    <p class="reason__text">A scalable network developed by over 1,500 engineers powers Corvanta business VoIP phone service. We promise top quality, security, and reliability.</p>
  </div>
  <div class="reason" style="left:29px;top:398px">
    <div class="reason__icon" role="img" aria-label="Office buildings icon"></div>
    <div class="reason__title">Designed for all industries</div>
    <p class="reason__text">There’s something for everyone. Our small business VoIP features benefit all industries, including insurance, hospitality, consulting firms, real estate, education, health care, and more!</p>
  </div>
  <div class="reason" style="left:29px;top:555px">
    <div class="reason__icon" role="img" aria-label="Innovation lightbulb icon"></div>
    <div class="reason__title">Innovation</div>
    <p class="reason__text">We are always innovating and improving our VoIP phone service. Your small business will always have the latest and greatest in business VoIP technology and phone systems.</p>
  </div>

  <div class="reason" style="left:348px;top:88px">
    <div class="reason__icon" role="img" aria-label="Support team icon"></div>
    <div class="reason__title">Amazing Service</div>
    <p class="reason__text">We are committed to delivering Amazing Service to your small business, at every point of contact you make with Corvanta. This is our brand promise.</p>
  </div>
  <div class="reason" style="left:348px;top:238px">
    <div class="reason__icon" role="img" aria-label="Smartphone icon"></div>
    <div class="reason__title">Mobile friendly</div>
    <p class="reason__text">Run your small business anywhere with the Corvanta app. Seamlessly text message your customers and team members right from your smartphone. Feel the power of business VoIP right at your fingertips.</p>
  </div>
  <div class="reason" style="left:348px;top:398px">
    <div class="reason__icon" role="img" aria-label="Headset agent icon"></div>
    <div class="reason__title">HD quality VoIP</div>
    <p class="reason__text">Experience crystal-clear HD voice quality with Corvanta’s small business VoIP phone service. You’ll never have to worry about poor call quality ever again.</p>
  </div>
  <div class="reason" style="left:348px;top:555px">
    <div class="reason__icon" role="img" aria-label="Gears and tools icon"></div>
    <div class="reason__title">Powerful features</div>
    <p class="reason__text">Get enterprise-grade business VoIP features without the hefty price tag. Auto-attendant, business text messaging, caller ID, voicemail to text, CRM integration, and much more.</p>
  </div>

  <div class="reason" style="left:666px;top:88px">
    <div class="reason__icon" role="img" aria-label="Desk phone icon"></div>
    <div class="reason__title">Easy to use</div>
    <p class="reason__text">Our business VoIP phones are so easy to use, you’ll be up and running within minutes. You don’t need to be a tech wizard or have an IT department to get the most out of your phone system. Corvanta was designed for non-technical small business owners.</p>
  </div>
  <div class="reason" style="left:666px;top:238px">
    <div class="reason__icon" role="img" aria-label="Price tag icon"></div>
    <div class="reason__title">Honest pricing</div>
    <p class="reason__text">Our customers know what they’re paying for. No contracts required, no hidden fees. You can cancel your service at any time, hassle-free.</p>
  </div>

  <div class="desk-phone abs" role="img" aria-label="Brontel KX-M41D desk phone" style="left:648px;top:395px;width:308px;height:250px"></div>
  <div class="dark-panel abs" style="left:632px;top:662px;width:324px;height:53px;display:flex;align-items:center;justify-content:center">
    <div class="logo" style="font-size:14px"><span class="logo__mark"></span>Pelomarc Systems</div>
  </div>
</section>

</body>
</html>
```